Meadowlark Learning Growth Partners (MLGP)

This is a professional business card. Logo and picture are a must on the front of the card. I am an educational consultant. I have been consulting for the past three years for a company. I am now opening my own company. My goal for my consulting company is to eventually consult all over America.

Target Market(s)

Educators, schools, professionals

Industry/Entity Type

Consulting

Contact Information for Business Card

Picture/logo on front, simple modern design

Font styles to use
Serif

Colors
85abd2
0355a3
3176b5
cedeed

Requirements
Must have
• picture, logo,
• Odessa Pruitt, Ed.S
• address 5073 Cormorant ridge Dr. Nashville, TN 37940
• Cell:616-555-0148
• Office: 629-555-0172
• www.Mlgpedu.example
• pruittodessa@mailbox.example

```html
<!DOCTYPE html>
<html lang="en">
<head>
<meta charset="utf-8">
<title>MLGP Business Card</title>
<link rel="stylesheet" href="https://fonts.googleapis.com/css2?family=Tinos:wght@400;700&display=swap">
<style>
  :root {
    --ink: #0355a3;
    --navy: #0b3f7f;
    --mid: #3176b5;
    --soft: #85abd2;
    --pale: #cedeed;
    --page: #f1f2f3;
    --photo-top: #c9d9ea;
    --photo-bottom: #8a7a70;
  }
  * { margin: 0; padding: 0; box-sizing: border-box; }
  html, body { width: 1200px; height: 1200px; overflow: hidden; }
  body {
    background: var(--page);
    position: relative;
    font-family: "Tinos", "Times New Roman", serif;
    color: var(--navy);
  }
  .card { position: absolute; overflow: hidden; }

  /* Front */
  .card-front {
    left: 82px; top: 144px; width: 680px; height: 442px;
    background: var(--pale);
  }
  .brand { position: absolute; left: 16px; top: 38px; display: flex; align-items: center; height: 84px; }
  .brand-dot { width: 58px; height: 58px; border-radius: 50%; background: var(--navy); margin-right: 14px; }
  .brand-name { font-weight: 700; font-size: 34px; letter-spacing: 2px; color: var(--navy); }
  .brand-rule { width: 2px; height: 84px; background: var(--navy); margin: 0 14px 0 14px; }
  .brand-tagline { font-weight: 700; font-size: 17px; line-height: 22px; color: var(--navy); }
  .contact { position: absolute; left: 14px; top: 192px; list-style: none; font-size: 23px; line-height: 31.5px; color: var(--navy); }
  .portrait {
    position: absolute; right: 0; top: 18px; width: 320px; height: 424px;
    background: linear-gradient(180deg, var(--photo-top) 0%, #d8c6ae 30%, #e6d6c8 50%, #26262c 72%, #1c1c22 100%);
  }

  /* Back */
  .card-back {
    left: 438px; top: 614px; width: 682px; height: 442px;
    background: linear-gradient(90deg, var(--pale) 0%, #b5cce6 50%, var(--soft) 100%);
  }
  .back-wave { position: absolute; inset: 0; width: 100%; height: 100%; }
  .back-mark { position: absolute; left: 72px; top: 22px; width: 262px; display: flex; flex-direction: column; align-items: center; }
  .back-dot { width: 170px; height: 170px; border-radius: 50%; background: var(--navy); margin-top: 36px; }
  .back-name { margin-top: 20px; font-weight: 700; font-size: 74px; letter-spacing: 4px; line-height: 1; color: var(--navy); }
</style>
</head>
<body>
  <section class="card card-front">
    <div class="brand">
      <div class="brand-dot"></div>
      <div class="brand-name">MLGP</div>
      <div class="brand-rule"></div>
      <div class="brand-tagline">Meadowlark<br>Learning<br>Growth<br>Partners</div>
    </div>
    <ul class="contact">
      <li>Odessa Pruitt, Ed.S</li>
      <li>address 5073 Cormorant ridge</li>
      <li>Dr. Nashville, TN 37940</li>
      <li>Cell:616-555-0148</li>
      <li>Office: 629-555-0172</li>
      <li>www.Mlgpedu.example</li>
      <li>pruittodessa@mailbox.example</li>
    </ul>
    <div class="portrait" role="img" aria-label="Portrait photo of Odessa Pruitt"></div>
  </section>

  <section class="card card-back">
    <svg class="back-wave" viewBox="0 0 568 368" preserveAspectRatio="none" aria-hidden="true">
      <path d="M0,255 C150,312 400,300 568,196 L568,368 L0,368 Z" fill="#e2ecf6"/>
      <path d="M0,268 C150,320 400,302 568,206 L568,368 L0,368 Z" fill="#85abd2"/>
      <path d="M0,290 C150,326 400,305 568,218 L568,368 L0,368 Z" fill="#3176b5"/>
    </svg>
    <div class="back-mark">
      <div class="back-dot"></div>
      <div class="back-name">MLGP</div>
    </div>
  </section>
</body>
</html>
```